Australian residential property business needs a business card design

I need a business card design for my new business 'Meadow Estate Partners'. The business will involve house purchases, land development sites, renovation projects, sub-divisions etc. I will be buying property from motivated vendors and working with property investors. I will deal with a wide range of people working in the residential property market including real estate agents, councils, tradespeople, banks, home owners, etc.

I would like something simple, not flashy, but a little bit unique. The colours should be in line with my logo. The business card needs to be professional. I would like something memorable, but not 'busy' or too bright. Not boring. Modern ok.

Target Market(s)

Home owners looking to sell their property, real estate agents, tradespeople (e.g. plumbers, builders, electricians etc), property investors, local councils, and anyone else involved in the residential property industry

Industry/Entity Type

Business

Contact Information for Business Card

I need to include my business name/logo, my name, my title, a PO Box number/address, a mobile number, and an email address.

Font styles to use
Serif

Requirements
Must have
• My business card details listed above.

```html
<!DOCTYPE html>
<html lang="en">
<head>
<meta charset="utf-8">
<title>Meadow Estate Partners – Business Card</title>
<link href="https://fonts.googleapis.com/css2?family=Open+Sans:wght@400;600;700&display=swap" rel="stylesheet">
<style>
  :root {
    --backdrop: #8e8e8e;
    --card-black: #000000;
    --contact-band: #111111;
    --accent-yellow: #f9cc2e;
    --stripe-white: #f4f4f4;
    --text-white: #f2f2f2;
  }
  * { box-sizing: border-box; margin: 0; padding: 0; }
  html, body { width: 1200px; height: 900px; overflow: hidden; }
  body {
    background: var(--backdrop);
    font-family: "Open Sans", Arial, sans-serif;
    position: relative;
  }
  .card {
    position: absolute;
    left: 260px;
    width: 680px;
    height: 388px;
    background: var(--card-black);
    overflow: hidden;
    box-shadow: 0 6px 18px rgba(0,0,0,.25);
  }
  .card--front { top: 40px; }
  .card--back { top: 472px; }
  .card__stripe {
    position: absolute; left: 0; right: 0; bottom: 54px; height: 9px;
    background: var(--stripe-white);
  }
  .card__band {
    position: absolute; left: 0; right: 0; bottom: 0; height: 54px;
    background: var(--accent-yellow);
  }
  .brand {
    display: flex; align-items: center; gap: 10px;
    color: var(--accent-yellow);
    font-weight: 700;
    text-transform: uppercase;
    letter-spacing: .5px;
  }
  .brand__dot {
    width: 16px; height: 16px; border-radius: 50%;
    background: var(--accent-yellow);
    flex: none;
  }
  .card--front .brand {
    position: absolute; top: 140px; left: 0; right: 0;
    justify-content: center; font-size: 26px;
  }
  .card--back .brand {
    position: absolute; top: 66px; left: 40px; font-size: 20px;
  }
  .holder {
    position: absolute; top: 70px; right: 44px; text-align: right;
  }
  .holder__name {
    color: var(--accent-yellow); font-weight: 700; font-size: 22px;
    text-transform: uppercase; letter-spacing: .3px;
  }
  .holder__title { color: var(--text-white); font-size: 16px; margin-top: 2px; }
  .contacts {
    position: absolute; left: 0; right: 0; top: 168px; bottom: 63px;
    background: var(--contact-band);
    display: flex; justify-content: space-between; align-items: flex-start;
    padding: 24px 40px 0;
    color: var(--text-white); font-size: 15px; line-height: 1.75;
  }
  .contacts__group { display: flex; flex-direction: column; }
  .contacts__group--phones { padding-top: 30px; }
  .contacts__group--online { padding-top: 60px; }
  .contact-line { display: flex; align-items: center; gap: 8px; }
  .contact-line--indent { padding-left: 20px; }
  .icon { width: 13px; height: 13px; fill: var(--accent-yellow); flex: none; }
</style>
</head>
<body>
  <section class="card card--front" aria-label="Business card front">
    <div class="brand"><span class="brand__dot"></span>Meadow Estate Partners</div>
    <div class="card__stripe"></div>
    <div class="card__band"></div>
  </section>

  <section class="card card--back" aria-label="Business card back">
    <div class="brand"><span class="brand__dot"></span>Meadow Estate Partners</div>
    <div class="holder">
      <div class="holder__name">Daniel Harper</div>
      <div class="holder__title">Managing Director</div>
    </div>
    <div class="contacts">
      <div class="contacts__group">
        <div class="contact-line">
          <svg class="icon" viewBox="0 0 12 12"><path d="M6 0a4 4 0 0 0-4 4c0 3 4 8 4 8s4-5 4-8a4 4 0 0 0-4-4zm0 5.6A1.6 1.6 0 1 1 6 2.4a1.6 1.6 0 0 1 0 3.2z"/></svg>
          1234, Address Goes Here,
        </div>
        <div class="contact-line">Country Name, 123456</div>
      </div>
      <div class="contacts__group contacts__group--phones">
        <div class="contact-line">
          <svg class="icon" viewBox="0 0 12 12"><path d="M1 4c0-1.5 2-2.5 5-2.5S11 2.5 11 4v1H8.5V4h-5v1H1zM2.5 6h7l1 4.5h-9z"/></svg>
          123.456.7890
        </div>
        <div class="contact-line">
          <svg class="icon" viewBox="0 0 12 12"><path d="M3 0h6v12H3zm1 1.5v7h4v-7z"/></svg>
          123.456.7890
        </div>
      </div>
      <div class="contacts__group contacts__group--online">
        <div class="contact-line">
          <svg class="icon" viewBox="0 0 12 12"><path d="M0 2h12v8H0zm1 1v.4l5 3 5-3V3z"/></svg>
          info@youremail.com
        </div>
        <div class="contact-line">
          <svg class="icon" viewBox="0 0 12 12"><path d="M1 8l3-3 1 1-3 3 1 1 3-3 1 1-3 3-3-3zm10-4L8 7 7 6l3-3-1-1-3 3-1-1 3-3z"/></svg>
          www.website.com
        </div>
      </div>
    </div>
    <div class="card__stripe"></div>
    <div class="card__band"></div>
  </section>
</body>
</html>
```